Business card design needed

Chasing a very simplistic modern design with a logo incorporating "TRV".
I'm starting a plumbing business.
I do water, sanitary and drainage plumbing that will cover residential, commercial, rental, rural, excavation, new housing and all maintanence requirements.

Industry/Entity Type

Business

Contact Information for Business Card

TRV PLUMBING SERVICES
DEAN HOLLOWBY - LICENSED PLUMBER
PHONE: 0481926574
E-MAIL: hollodt7@wirelane.com
NORTHERN SUBURBS

Requirements
Must have
• lower case email address

```html
<!DOCTYPE html>
<html lang="en">
<head>
<meta charset="utf-8">
<title>TRV Plumbing Services – Business Card</title>
<link rel="stylesheet" href="https://fonts.googleapis.com/css2?family=Arimo:wght@400;700&display=swap">
<style>
  :root {
    --stage: #2b2b2d;
    --card-dark: #1d1d1f;
    --card-dark-soft: #242426;
    --brand-blue: #1e9be0;
    --band-blue: #2aa3e3;
    --rule-grey: #a9abae;
    --tag-grey: #b4b6b9;
    --ink: #1a1a1c;
  }
  * { box-sizing: border-box; margin: 0; padding: 0; }
  html, body {
    width: 1200px;
    height: 900px;
    overflow: hidden;
    background: var(--stage);
    font-family: "Arimo", Arial, sans-serif;
  }
  .stage {
    position: relative;
    width: 1200px;
    height: 900px;
  }
  .card {
    position: absolute;
    width: 560px;
    height: 320px;
    background: var(--card-dark);
    overflow: hidden;
    box-shadow: 0 14px 30px rgba(0,0,0,0.45);
  }
  .card--front { left: 150px; top: 95px; }
  .card--back  { left: 490px; top: 485px; }

  .texture {
    position: absolute;
    inset: 0;
    background: linear-gradient(135deg, var(--card-dark-soft), var(--card-dark));
  }

  /* Front */
  .front-logo {
    position: absolute;
    left: 0; right: 0;
    top: 92px;
    text-align: center;
  }
  .front-logo .brand-name {
    display: block;
    font-weight: 700;
    font-size: 108px;
    line-height: 0.9;
    letter-spacing: -2px;
    color: var(--brand-blue);
  }
  .front-logo .brand-tag {
    display: block;
    margin-top: 8px;
    font-weight: 700;
    font-size: 25px;
    letter-spacing: 1px;
    color: var(--tag-grey);
  }

  /* Back */
  .back-top {
    position: absolute;
    left: 0; top: 0;
    width: 100%;
    height: 128px;
  }
  .back-logo {
    position: absolute;
    left: 34px;
    top: 38px;
    display: flex;
    align-items: flex-end;
    gap: 10px;
  }
  .back-logo .brand-name {
    font-weight: 700;
    font-size: 74px;
    line-height: 0.8;
    letter-spacing: -1px;
    color: var(--brand-blue);
  }
  .back-logo .brand-tag {
    font-weight: 700;
    font-size: 19px;
    line-height: 1;
    color: var(--tag-grey);
    padding-bottom: 24px;
  }
  .rule {
    position: absolute;
    left: 0; top: 128px;
    width: 100%;
    height: 6px;
    background: var(--rule-grey);
  }
  .band {
    position: absolute;
    left: 0; top: 134px;
    width: 100%;
    height: 186px;
    background: var(--band-blue);
    color: var(--ink);
    padding: 28px 40px;
  }
  .person-name {
    font-weight: 700;
    font-size: 25px;
    letter-spacing: 0.5px;
  }
  .person-role {
    font-weight: 700;
    font-size: 14px;
    margin-top: 2px;
  }
  .contact {
    margin-top: 30px;
    font-weight: 700;
    font-size: 15px;
    line-height: 1.35;
  }
</style>
</head>
<body>
<main class="stage">
  <section class="card card--front" aria-label="Business card front">
    <div class="texture"></div>
    <div class="front-logo">
      <span class="brand-name">TRV</span>
      <span class="brand-tag">PLUMBING SERVICES</span>
    </div>
  </section>

  <section class="card card--back" aria-label="Business card back">
    <div class="back-top texture"></div>
    <div class="back-logo">
      <span class="brand-name">TRV</span>
      <span class="brand-tag">PLUMBING<br>SERVICES</span>
    </div>
    <div class="rule"></div>
    <div class="band">
      <p class="person-name">DEAN HOLLOWBY</p>
      <p class="person-role">LICENSED PLUMBER</p>
      <p class="contact">P: 0481926574 &nbsp;E: hollodt7@wirelane.com<br>NORTHERN SUBURBS</p>
    </div>
  </section>
</main>
</body>
</html>
```